12 Page a3 Poster Menu For Cafe & Convenience Store

Cafe / Diner in City location needs a menu design.

We now need a 12 page A3 size menu design.

We have uploaded how the menu will look, with all the 12 posters (all A3 paper size portrait)

check attachment "12 A3 poster [url removed, login to view]" for menu layout'

Poster 1 Logo & trading hours / phone
Poster 2 Coffee Menu (coffee [url removed, login to view])
Poster 3 Coffee & Cake Menu (cakes a3 [url removed, login to view])

Poster 4 Bread Menu (bread [url removed, login to view])
Poster 5 Meat / Protein Menu (meat and protein [url removed, login to view])
Poster 6 Salads Menu (salad [url removed, login to view])

Poster 7 = Falafel Wrap Sandwich ( to be uploaded soon)
Poster 8 = Hot Dog Special (hotdog [url removed, login to view])
Poster 9 = Pies and Pasties prices (still to be uploaded soon)

Poster 10,11,12 still to be uploaded soon

```html
<!DOCTYPE html>
<html lang="en">
<head>
<meta charset="utf-8">
<title>Coffee Menu Poster</title>
<link href="https://fonts.googleapis.com/css2?family=Dancing+Script:wght@500;700&family=Pacifico&display=swap" rel="stylesheet">
<style>
  :root {
    --ink-dark: #17120f;
    --stripe-a: #3a2c22;
    --stripe-b: #4c3a2d;
    --stripe-c: #2a201a;
    --lime: #8cc63f;
    --lime-light: #a8d65a;
    --lime-deep: #5f9a22;
    --cream: #ffffff;
    --coffee-brown: #7b4a1d;
    --photo-light: #f4f1ed;
    --photo-mid: #d9c6b2;
  }
  html, body {
    margin: 0;
    padding: 0;
    overflow: hidden;
    background: var(--ink-dark);
  }
  .poster {
    position: relative;
    width: 849px;
    height: 1200px;
    overflow: hidden;
    background: var(--ink-dark);
    font-family: "Dancing Script", cursive;
  }
  .poster-art {
    position: absolute;
    inset: 0;
  }
  .menu-list {
    position: absolute;
    left: 28px;
    top: 38px;
    margin: 0;
    padding: 0;
    list-style: none;
    color: var(--cream);
    font-size: 46px;
    font-weight: 500;
    line-height: 64.5px;
  }
  .menu-list li { white-space: nowrap; }
  .menu-list .price { margin-left: 38px; }
  .brand-name {
    position: absolute;
    left: 644px;
    top: 1034px;
    width: 190px;
    text-align: center;
    white-space: nowrap;
    color: var(--cream);
    font-family: "Dancing Script", cursive;
    font-weight: 700;
    font-size: 38px;
    line-height: 48px;
    transform: rotate(-5deg);
  }
</style>
</head>
<body>
<div class="poster">
  <svg class="poster-art" width="849" height="1200" viewBox="0 0 849 1200" xmlns="http://www.w3.org/2000/svg">
    <defs>
      <radialGradient id="photo-fill" cx="50%" cy="45%" r="55%">
        <stop offset="0%" stop-color="var(--photo-mid)"/>
        <stop offset="100%" stop-color="var(--photo-light)"/>
      </radialGradient>
    </defs>
    <rect x="330" y="0" width="519" height="1200" fill="var(--stripe-a)"/>
    <rect x="470" y="0" width="60" height="1200" fill="var(--stripe-b)"/>
    <rect x="560" y="0" width="24" height="1200" fill="var(--stripe-c)"/>
    <rect x="640" y="0" width="18" height="1200" fill="var(--stripe-b)"/>
    <rect x="690" y="0" width="46" height="1200" fill="var(--stripe-c)"/>
    <rect x="760" y="0" width="20" height="1200" fill="var(--stripe-b)"/>
    <rect x="805" y="0" width="44" height="1200" fill="var(--stripe-c)"/>
    <path d="M0 0 H320 C250 260 300 560 420 760 C540 930 700 960 849 975 V1200 H0 Z" fill="var(--ink-dark)"/>
    <path d="M320 0 C250 260 300 560 420 760 C540 930 700 960 849 975" fill="none" stroke="var(--lime)" stroke-width="4"/>
    <circle cx="566" cy="250" r="252" fill="var(--lime)"/>
    <circle cx="566" cy="250" r="240" fill="url(#photo-fill)" role="img" aria-label="Photo of a cappuccino with latte art in a white cup on a saucer"/>
    <path d="M0 905 C180 940 380 1000 500 1010 L500 1080 C380 1070 180 1010 0 980 Z" fill="var(--lime-light)"/>
    <path d="M470 960 C600 950 720 940 849 945 V1040 C720 1030 600 1040 470 1050 Z" fill="var(--lime)"/>
    <path d="M0 980 C180 1010 380 1070 500 1080 L470 1050 Z" fill="var(--lime-deep)"/>
    <rect x="644" y="985" width="190" height="150" rx="10" fill="var(--stripe-b)" transform="rotate(-5 739 1060)"/>
    <text x="30" y="1155" font-family="Pacifico, cursive" font-size="128" fill="var(--cream)" stroke="var(--coffee-brown)" stroke-width="12" paint-order="stroke" stroke-linejoin="round">Coffee</text>
  </svg>

  <ul class="menu-list">
    <li>Cappacino</li>
    <li>Latte’</li>
    <li>Espresso</li>
    <li>Machiatto</li>
    <li>Decaf</li>
    <li>Chai Latte’</li>
    <li>Short/Long Black</li>
    <li>Hot Chocolate</li>
    <li>Mochachino/Latte’</li>
    <li>Selection of Tea/Herbal</li>
    <li>Small(Single Shot)<span class="price">3.5</span></li>
    <li>Medium(Double Shot)<span class="price">4.0</span></li>
    <li>Large 4.5(Triple Shot)<span class="price">4.5</span></li>
    <li>Syrups / Soy<span class="price">+0.5</span></li>
  </ul>

  <div class="brand-name">Nine Lanes</div>
</div>
</body>
</html>
```